11x 11 - KIVO Program Flyer

Introducing The KIVO PROGRAM

The BEST DPA Product on the Planet
* Lowest Zarn in the Industry - 580 Minimum
* Nothing Down - 100% GTU Purchase Financing
* One Submission, One Approval and One Closing
* No Income Limits, No DTI Restrictions, No Property Restrictions

Call (800) 471-9026 for more information

RLCB #738160
www.2ndlanehomes.com

```html
<!DOCTYPE html>
<html lang="en">
<head>
<meta charset="utf-8">
<title>KIVO Program Flyer</title>
<link rel="stylesheet" href="https://fonts.googleapis.com/css2?family=Anton&family=Montserrat:wght@300;400;600;700;800;900&display=swap">
<style>
:root{
  --blue:#1b5fa0;
  --gold:#a9a049;
  --ink:#111111;
  --white:#ffffff;
  --page:#ececec;
  --photo-a:#c9a58a;
  --photo-b:#7b6a5c;
}
*{margin:0;padding:0;box-sizing:border-box}
html,body{width:1091px;height:1200px;overflow:hidden;background:var(--page)}
.flyer{position:absolute;left:94px;top:149px;width:902px;height:902px;overflow:hidden;
  background:linear-gradient(160deg,#ffffff 0%,#f4f5f7 45%,#e9ebee 62%,#f7f8f9 80%,#ffffff 100%);
  font-family:"Montserrat",sans-serif;color:var(--ink)}
.headline-intro{position:absolute;left:29px;top:22px;font-family:"Anton",sans-serif;font-size:58px;line-height:1;color:var(--blue);letter-spacing:0.5px}
.headline-the{position:absolute;left:24px;top:103px;font-family:"Montserrat",sans-serif;font-weight:400;font-size:44px;line-height:1;transform:rotate(-90deg);transform-origin:center;width:80px;text-align:center}
.headline-name{position:absolute;left:82px;top:70px;font-family:"Montserrat",sans-serif;font-weight:900;font-size:100px;line-height:1;color:var(--gold);letter-spacing:-1px}
.headline-tag{position:absolute;left:38px;top:166px;font-weight:800;font-size:21.5px;line-height:1}
.headline-program{position:absolute;left:29px;top:190px;font-family:"Anton",sans-serif;font-size:76px;line-height:1;color:var(--blue)}
.ribbon{position:absolute;left:0;top:290px;width:400px;height:90px}
.ribbon-text{position:absolute;left:29px;top:300px;color:var(--white)}
.ribbon-text .lead{font-size:22px;font-weight:400}
.ribbon-text .big{font-size:39px;font-weight:800;letter-spacing:0.5px}
.ribbon-text .sub{font-size:22px;font-weight:400;margin-top:-4px}
.features{position:absolute;left:30px;top:410px;list-style:none}
.feature{display:flex;align-items:center;height:77px;margin-bottom:21px}
.feature:nth-child(2){margin-bottom:19px}
.feature:nth-child(3){margin-bottom:23px}
.feature-icon{width:82px;height:77px;background:var(--blue);display:flex;align-items:center;justify-content:center;flex:none}
.feature-text{margin-left:27px;font-weight:600;font-size:19.5px;line-height:25px;letter-spacing:0.4px}
.cta{position:absolute;left:0;top:803px;width:464px;height:86px}
.cta-text{position:absolute;left:30px;top:806px;color:var(--white)}
.cta-phone{font-family:"Anton",sans-serif;font-size:44px;line-height:1.05;letter-spacing:0.3px}
.cta-more{font-weight:500;font-size:24.5px;letter-spacing:1px;line-height:1}
.side-strip{position:absolute;left:579px;top:0;width:234px;height:683px;background:var(--blue);border-radius:0 0 117px 117px}
.badge{position:absolute;left:641px;top:20px;width:110px;height:110px;border:12px solid var(--white)}
.photo-ring{position:absolute;left:500px;top:197px;width:392px;height:392px;border-radius:50%;background:var(--white)}
.photo-ring-inner{position:absolute;left:512px;top:209px;width:368px;height:368px;border-radius:50%;border:8px solid var(--blue);background:var(--white)}
.photo{position:absolute;left:526px;top:223px;width:340px;height:340px;border-radius:50%;
  background:radial-gradient(circle at 50% 40%,#e8dfd6 0%,var(--photo-a) 45%,var(--photo-b) 100%)}
.license{position:absolute;left:579px;top:594px;width:234px;text-align:center;color:var(--white);line-height:1.05}
.license-label{font-weight:500;font-size:29px;letter-spacing:1px}
.license-num{font-weight:800;font-size:29px;letter-spacing:1px}
.company{position:absolute;left:579px;top:760px;width:234px;display:flex;align-items:center;justify-content:center;gap:8px;color:var(--blue);font-weight:700;font-size:17px}
.company-dot{width:14px;height:14px;border-radius:50%;background:var(--gold);flex:none}
.website{position:absolute;left:548px;top:828px;width:300px;text-align:center;font-family:"Anton",sans-serif;font-size:29px;line-height:1;color:var(--ink)}
</style>
</head>
<body>
<main class="flyer">
  <h1>
    <span class="headline-intro">INTRODUCING</span>
    <span class="headline-the">the</span>
    <span class="headline-name">KIVO</span>
    <span class="headline-tag">When “Nothing” is all you need</span>
    <span class="headline-program">PROGRAM</span>
  </h1>

  <svg class="ribbon" viewBox="0 0 400 90" aria-hidden="true">
    <path d="M0 5 H330 Q345 5 355 18 L396 84 H0 Z" fill="#cfcfcf" opacity="0.6" transform="translate(0 4)"/>
    <path d="M0 0 H330 Q345 0 355 13 L396 84 H0 Z" fill="#a9a049"/>
  </svg>
  <div class="ribbon-text">
    <div><span class="lead">The </span><span class="big">BEST DPA</span></div>
    <div class="sub">Product on the Planet</div>
  </div>

  <ul class="features">
    <li class="feature">
      <span class="feature-icon">
        <svg width="56" height="48" viewBox="0 0 56 48" aria-hidden="true">
          <path d="M6 44 A24 24 0 1 1 50 30" fill="none" stroke="#fff" stroke-width="8"/>
          <line x1="28" y1="30" x2="38" y2="10" stroke="#fff" stroke-width="3"/>
          <circle cx="27" cy="31" r="4" fill="none" stroke="#fff" stroke-width="2.5"/>
        </svg>
      </span>
      <span class="feature-text">LOWEST ZARN<br>IN THE INDUSTRY<br>580 MINIMUM</span>
    </li>
    <li class="feature">
      <span class="feature-icon">
        <svg width="56" height="60" viewBox="0 0 56 60" aria-hidden="true">
          <path d="M18 4 L24 9 L28 3 L32 9 L38 4 L36 14 H20 Z" fill="#fff"/>
          <path d="M20 17 H36 C50 24 56 40 52 50 C50 56 44 58 28 58 C12 58 6 56 4 50 C0 40 6 24 20 17 Z" fill="#fff"/>
          <text x="28" y="48" text-anchor="middle" font-family="Montserrat,sans-serif" font-weight="800" font-size="22" fill="#1b5fa0">$</text>
        </svg>
      </span>
      <span class="feature-text">NOTHING DOWN,<br>100% GTU PURCHASE<br>FINANCING</span>
    </li>
    <li class="feature">
      <span class="feature-icon">
        <svg width="34" height="48" viewBox="0 0 34 48" aria-hidden="true">
          <path d="M6 24 V12 a3 3 0 0 1 6 0 V8 a3 3 0 0 1 6 0 V6 a3 3 0 0 1 6 0 V10 a3 3 0 0 1 6 0 V32 C30 42 24 46 17 46 C10 46 4 42 4 34 Z" fill="none" stroke="#fff" stroke-width="2.2" stroke-linejoin="round"/>
          <path d="M12 12 V24 M18 8 V24 M24 8 V24" stroke="#fff" stroke-width="2"/>
        </svg>
      </span>
      <span class="feature-text">NO INCOME LIMITS,<br>NO DTI RESTRICTIONS,<br>NO PROPERTY RESTRICTIONS</span>
    </li>
    <li class="feature">
      <span class="feature-icon">
        <svg width="54" height="52" viewBox="0 0 54 52" aria-hidden="true">
          <rect x="3" y="3" width="38" height="38" fill="none" stroke="#fff" stroke-width="3"/>
          <path d="M10 14 H34 M10 21 H30 M10 28 H22" stroke="#fff" stroke-width="3"/>
          <circle cx="38" cy="36" r="13" fill="#1b5fa0" stroke="#fff" stroke-width="3"/>
          <path d="M32 36 L37 41 L45 31" fill="none" stroke="#fff" stroke-width="3"/>
        </svg>
      </span>
      <span class="feature-text">ONE SUBMISSION,<br>ONE APPROVAL<br>&amp; ONE CLOSING</span>
    </li>
  </ul>

  <svg class="cta" viewBox="0 0 464 86" aria-hidden="true">
    <path d="M0 0 H395 Q410 0 418 12 L464 86 H0 Z" fill="#1b5fa0"/>
  </svg>
  <div class="cta-text">
    <div class="cta-phone">CALL (800) 471-9026</div>
    <div class="cta-more">FOR MORE INFORMATION</div>
  </div>

  <div class="side-strip"></div>
  <div class="badge" aria-hidden="true"></div>
  <div class="photo-ring"></div>
  <div class="photo-ring-inner"></div>
  <div class="photo" role="img" aria-label="Photo of a joyful couple unpacking moving boxes in their new living room"></div>
  <div class="license">
    <div class="license-label">RLCB</div>
    <div class="license-num">738160</div>
  </div>

  <div class="company"><span class="company-dot"></span><span>2nd Lane Financial, Inc.</span></div>
  <div class="website">WWW.2NDLANEHOMES.COM</div>
</main>
</body>
</html>
```